Frostvale Cool Packs needs stationery designed for their new logo

We have a new logo so now want all our stationery to be redesigned.
Frostvale is a gel ice pack product used by the seafood & food industry to transport chilled products around the world.

We would like to use our new logo with icy or snow backgrounds or elements.
Our company tag line is "Keep your products chilled for longer"
I'll attach our old business cards so that you can use the text off them.
2nd attachment is our new logo to be used.

We want a design for:
- Business cards
- Letter Head
- Email signature

Target Market(s)

seafood & chilled food distributors

Industry/Entity Type

Industry

Font styles to use
Sans Serif

Colors
0492cd
85cae6
cee9f5

Requirements
Must have
• Our logo
Nice to have
• Snow or ice background or image incorporated somehow

```html
<!DOCTYPE html>
<html lang="en">
<head>
<meta charset="utf-8">
<title>Frostvale Cool Packs – Stationery</title>
<link rel="stylesheet" href="https://fonts.googleapis.com/css2?family=Mulish:wght@400;600;700&family=Roboto+Condensed:wght@400&display=swap">
<style>
  :root{
    --board:#a6a6a6;
    --brand:#0492cd;
    --brand-deep:#0a6fbe;
    --ice:#85cae6;
    --frost:#cee9f5;
    --ink:#1f2a33;
    --grey:#6d7478;
    --white:#ffffff;
    --shadow:4px 6px 10px rgba(0,0,0,.35);
  }
  *{margin:0;padding:0;box-sizing:border-box}
  html,body{width:1200px;height:1200px;overflow:hidden;background:var(--board)}
  body{position:relative;font-family:"Mulish",sans-serif;color:var(--ink)}
  .piece{position:absolute;overflow:hidden;box-shadow:var(--shadow);background:var(--white)}
  .abs{position:absolute;line-height:1;white-space:nowrap}
  .cond{font-family:"Roboto Condensed",sans-serif}
  .wordmark{font-family:"Mulish",sans-serif;font-weight:700;letter-spacing:.2px}
  .icon{width:1em;height:1em;vertical-align:-.12em;margin-right:.45em}
  .contact{font-family:"Roboto Condensed",sans-serif}

  /* business cards */
  .card{width:346px;height:213px}
  .card--blue{background:linear-gradient(180deg,#2f8fd6 0%,#1679c8 55%,var(--brand-deep) 100%);color:var(--white)}
  .frost-field{position:absolute;left:0;top:0;width:100%;height:120px;
    background:linear-gradient(180deg,rgba(255,255,255,.22),rgba(255,255,255,0))}
  .frost-field--light{height:180px;background:linear-gradient(180deg,#cfe6f0 0%,#e9f4f9 45%,#ffffff 100%)}
  .frost-corner{position:absolute;right:0;bottom:0;width:120px;height:110px;
    background:radial-gradient(circle at 70% 70%,rgba(255,255,255,.22),rgba(255,255,255,0) 70%)}
  .frost-corner--light{background:radial-gradient(circle at 70% 70%,rgba(133,202,230,.45),rgba(133,202,230,0) 70%)}
  .tag-band{position:absolute;left:0;bottom:0;width:100%;height:24px;background:var(--brand-deep);
    color:var(--white);font-family:"Roboto Condensed",sans-serif;font-size:13px;text-align:center;line-height:24px}
  .ice-band{position:absolute;left:0;width:100%;
    background:linear-gradient(100deg,#a9d6ee 0%,#d6edf8 25%,#8cc6e6 50%,#cde8f6 75%,#9fd0ec 100%)}

  .name{font-weight:700;color:var(--brand-deep)}
  .card--blue .name{color:var(--white)}
</style>
</head>
<body>

<svg width="0" height="0" style="position:absolute" aria-hidden="true">
  <symbol id="i-mail" viewBox="0 0 16 16">
    <rect x="1.5" y="4" width="13" height="9" rx="1" fill="currentColor"/>
    <path d="M1.8 4.5 8 9.5l6.2-5" fill="none" stroke="#fff" stroke-width="1.3"/>
  </symbol>
  <symbol id="i-web" viewBox="0 0 16 16">
    <g fill="none" stroke="currentColor" stroke-width="1.4">
      <circle cx="8" cy="8" r="6.3"/><ellipse cx="8" cy="8" rx="2.7" ry="6.3"/>
      <path d="M1.7 8h12.6M2.8 4.8h10.4M2.8 11.2h10.4"/>
    </g>
  </symbol>
</svg>

<!-- Card 1 -->
<section class="piece card card--blue" style="left:103px;top:46px">
  <div class="frost-field" role="img" aria-label="Snowflake frost pattern"></div>
  <div class="frost-corner" role="img" aria-label="Large soft snowflake shape"></div>
  <div class="abs wordmark" style="right:21px;top:15px;font-size:23px">Frostvale</div>
  <div class="abs cond" style="right:21px;top:63px;font-size:13px">Keep your products chilled for longer</div>
  <div class="abs name" style="left:21px;top:128px;font-size:14px">Marcus Hale</div>
  <div class="abs cond" style="left:21px;top:146px;font-size:10px">Business Development</div>
  <div class="abs contact" style="left:19px;top:169px;font-size:9.5px"><svg class="icon"><use href="#i-mail"/></svg>marcus.hale@frostvale.com.au</div>
  <div class="abs contact" style="left:19px;top:181px;font-size:9.5px"><svg class="icon"><use href="#i-web"/></svg>www.frostvale.com.au</div>
</section>

<!-- Card 2 -->
<section class="piece card" style="left:103px;top:350px">
  <div class="frost-field frost-field--light" role="img" aria-label="Light snowflake frost pattern"></div>
  <div class="frost-corner frost-corner--light" style="bottom:24px" role="img" aria-label="Large soft snowflake shape"></div>
  <div class="abs name" style="left:25px;top:21px;font-size:14px">Marcus Hale</div>
  <div class="abs cond" style="left:25px;top:38px;font-size:10px">Business Development</div>
  <div class="abs wordmark" style="right:21px;top:28px;font-size:19px;color:var(--brand-deep)">Frostvale</div>
  <div class="abs contact" style="left:26px;top:151px;font-size:9.5px"><svg class="icon" style="color:var(--brand-deep)"><use href="#i-mail"/></svg>marcus.hale@frostvale.com.au</div>
  <div class="abs contact" style="left:26px;top:163px;font-size:9.5px"><svg class="icon" style="color:var(--brand-deep)"><use href="#i-web"/></svg>www.frostvale.com.au</div>
  <div class="tag-band">Keep your products chilled for longer</div>
</section>

<!-- Card 3 -->
<section class="piece card card--blue" style="left:103px;top:646px">
  <div class="frost-field" role="img" aria-label="Snowflake frost pattern"></div>
  <div class="frost-corner" role="img" aria-label="Large soft snowflake shape"></div>
  <div class="abs wordmark" style="left:64px;top:20px;font-size:34px">Frostvale</div>
  <div class="abs cond" style="right:61px;top:65px;font-size:12px">Keep your products chilled for longer</div>
  <div class="abs name" style="left:27px;top:136px;font-size:14px">Marcus Hale</div>
  <div class="abs cond" style="left:27px;top:153px;font-size:10px">Business Development</div>
  <div class="abs contact" style="left:27px;top:175px;font-size:9.5px"><svg class="icon"><use href="#i-mail"/></svg>marcus.hale@frostvale.com.au</div>
  <div class="abs contact" style="left:27px;top:187px;font-size:9.5px"><svg class="icon"><use href="#i-web"/></svg>www.frostvale.com.au</div>
</section>

<!-- Card 4 -->
<section class="piece card" style="left:103px;top:941px">
  <div class="abs name" style="left:25px;top:42px;font-size:14px">Marcus Hale</div>
  <div class="abs cond" style="left:25px;top:59px;font-size:10px">Business Development</div>
  <div class="abs contact" style="left:157px;top:43px;font-size:9.5px"><svg class="icon" style="color:var(--brand-deep)"><use href="#i-mail"/></svg>marcus.hale@frostvale.com.au</div>
  <div class="abs contact" style="left:157px;top:55px;font-size:9.5px"><svg class="icon" style="color:var(--brand-deep)"><use href="#i-web"/></svg>www.frostvale.com.au</div>
  <div class="ice-band" style="top:103px;height:110px" role="img" aria-label="Cracked ice texture"></div>
  <div class="abs wordmark" style="left:0;width:100%;text-align:center;top:130px;font-size:26px;color:var(--brand-deep)">Frostvale</div>
  <div class="abs" style="left:0;width:100%;text-align:center;top:180px;font-size:13.5px;font-weight:600">Keep your products chilled for longer</div>
</section>

<!-- Letterhead -->
<section class="piece" style="left:553px;top:46px;width:517px;height:730px">
  <div class="abs wordmark" style="left:0;width:100%;text-align:center;top:41px;font-size:23px;color:var(--brand-deep)">Frostvale</div>
  <div class="abs" style="left:139px;top:263px;width:240px;height:244px;border-radius:50%;
       background:radial-gradient(circle,rgba(206,233,245,.55),rgba(206,233,245,0) 70%)"
       role="img" aria-label="Faint snowflake watermark"></div>
  <div class="abs" style="left:97px;top:690px;font-size:7px">
    <span class="name" style="font-size:8px">Marcus Hale</span>
    <span class="cond" style="color:var(--ink)"> | Business Development</span>
    <span class="contact" style="margin-left:12px"><svg class="icon" style="color:var(--brand-deep)"><use href="#i-mail"/></svg>marcus.hale@frostvale.com.au</span>
    <span class="contact" style="margin-left:8px"><svg class="icon" style="color:var(--brand-deep)"><use href="#i-web"/></svg>www.frostvale.com.au</span>
  </div>
  <div class="ice-band" style="top:704px;height:26px" role="img" aria-label="Cracked ice texture"></div>
  <div class="abs cond" style="left:0;width:100%;text-align:center;top:713px;font-size:9px">KEEP YOUR PRODUCTS CHILLED FOR LONGER</div>
</section>

<!-- Email signature 1 -->
<section class="piece" style="left:520px;top:812px;width:608px;height:106px">
  <div class="abs cond" style="left:11px;top:9px;font-size:14px;color:var(--grey)">Best regards</div>
  <div class="abs name" style="left:11px;top:31px;font-size:18px">Marcus Hale</div>
  <div class="abs cond" style="left:11px;top:53px;font-size:15px">Business Development</div>
  <div class="abs" style="left:156px;top:28px;width:1px;height:44px;background:var(--ice)"></div>
  <div class="abs contact" style="left:166px;top:32px;font-size:14px"><svg class="icon" style="color:var(--brand-deep)"><use href="#i-mail"/></svg>marcus.hale@frostvale.com.au</div>
  <div class="abs contact" style="left:166px;top:51px;font-size:14px"><svg class="icon" style="color:var(--brand-deep)"><use href="#i-web"/></svg>www.frostvale.com.au</div>
  <div class="abs" style="left:406px;top:28px;width:1px;height:44px;background:var(--ice)"></div>
  <div class="abs wordmark" style="left:424px;top:38px;font-size:24px;color:var(--brand-deep)">Frostvale</div>
  <div class="ice-band" style="top:82px;height:24px" role="img" aria-label="Cracked ice texture"></div>
</section>

<!-- Email signature 2 -->
<section class="piece" style="left:520px;top:953px;width:612px;height:76px">
  <div class="abs cond" style="left:11px;top:7px;font-size:14px;color:var(--grey)">Best regards</div>
  <div class="abs name" style="left:11px;top:27px;font-size:18px">Marcus Hale</div>
  <div class="abs cond" style="left:11px;top:49px;font-size:15px">Business Development</div>
  <div class="abs" style="left:156px;top:24px;width:1px;height:44px;background:var(--ice)"></div>
  <div class="abs contact" style="left:166px;top:28px;font-size:14px"><svg class="icon" style="color:var(--brand-deep)"><use href="#i-mail"/></svg>marcus.hale@frostvale.com.au</div>
  <div class="abs contact" style="left:166px;top:47px;font-size:14px"><svg class="icon" style="color:var(--brand-deep)"><use href="#i-web"/></svg>www.frostvale.com.au</div>
  <div class="abs" style="left:406px;top:24px;width:1px;height:44px;background:var(--ice)"></div>
  <div class="abs wordmark" style="left:424px;top:34px;font-size:24px;color:var(--brand-deep)">Frostvale</div>
</section>

<!-- Email signature 3 -->
<section class="piece" style="left:520px;top:1054px;width:461px;height:95px">
  <div class="abs name" style="left:11px;top:8px;font-size:18px">Marcus Hale</div>
  <div class="abs cond" style="left:11px;top:30px;font-size:15px">Business Development</div>
  <div class="abs contact" style="left:11px;top:52px;font-size:14px"><svg class="icon" style="color:var(--brand-deep)"><use href="#i-mail"/></svg>marcus.hale@frostvale.com.au</div>
  <div class="abs contact" style="left:11px;top:71px;font-size:14px"><svg class="icon" style="color:var(--brand-deep)"><use href="#i-web"/></svg>www.frostvale.com.au</div>
  <div class="abs" style="left:258px;top:8px;width:1px;height:80px;background:var(--ice)"></div>
  <div class="abs wordmark" style="left:274px;top:40px;font-size:24px;color:var(--brand-deep)">Frostvale</div>
</section>

</body>
</html>
```